Design a Mobile First Website for a Salad Resturant

** WEBSITE LIKE AN APP, NOT LANDING PAGE **

1. Homepage
Objective: Introduce the brand and direct visitors to either start creating their custom salad or explore the menu of pre-designed salads.
Design Elements:
Clean and minimalistic layout with high-quality images of fresh salads.
Two prominent buttons: "Create Your Salad" and "Our Salads".
Brief welcome message that highlights the freshness and quality of ingredients.

2. Create Your Salad Page
Objective: Allow customers to design their salad from a list of ingredients.
Design Elements:
Interactive, step-by-step builder interface where customers can select ingredients. Each ingredient category (like greens, proteins, toppings, dressings) should be a separate step in the process.
Visual representation of their salad being built as they select ingredients.
Information icons next to each ingredient for dietary information (e.g., vegan, gluten-free, calories).
Option to save favorite combinations or reorder past salads.
Clear price updates as they add or remove ingredients.

3. Our Salads Page
Objective: Showcase a list of pre-designed salad options that customers can quickly choose from.
Design Elements:
Grid layout with images and brief descriptions of each pre-designed salad.
Include customer reviews and ratings for each salad.
Easy "Add to Cart" option from this page.

4. Cart and Checkout Page
Objective: Streamline the checkout process with minimal steps.
Design Elements:
Summary of order with options to modify quantities or remove items.
Simple form for entering delivery details, with the ability to remember details for returning customers.
Secure payment gateway integration.
A confirmation screen with estimated delivery time and order tracking capabilities.

5. Mobile Optimization
Approach: Since this is a "Mobile First Design", ensure that:
The website is responsive and elements like buttons, text, and images scale properly across different devices.
Touch-friendly interfaces with large tap targets for ease of use on mobile devices.
Fast loading times by optimizing images and using mobile-first coding practices.

Target Market(s)

Food

Industry/Entity Type

Food

Number of Pages Required

4 page

Requirements
Must have
• Modren Design, Mobile First

```html
<!DOCTYPE html>
<html lang="en">
<head>
<meta charset="UTF-8">
<title>Verdo – Salad App Screens</title>
<link rel="stylesheet" href="https://fonts.googleapis.com/css2?family=Lexend:wght@400;500;600;700&display=swap">
<style>
  :root{
    --bg-top:#0f5a3a;
    --bg-bottom:#2aa173;
    --sage:#c3d1a6;
    --sage-soft:#dfe7cd;
    --olive-ink:#2e3a12;
    --ink:#1d1d1d;
    --muted:#7a7a7a;
    --orange:#e2a56c;
    --slate:#4a5e77;
    --dot-olive:#9aab74;
    --star:#e2ad17;
    --star-off:#c9c9c9;
    --white:#ffffff;
  }
  *{box-sizing:border-box;margin:0;padding:0}
  html,body{width:1143px;height:1200px;overflow:hidden}
  body{
    font-family:"Lexend",sans-serif;
    background:linear-gradient(180deg,var(--bg-top),var(--bg-bottom));
    position:relative;
  }
  .screen{
    position:absolute;top:38px;width:510px;height:1124px;overflow:hidden;
    background:linear-gradient(170deg,#f6f5ef 0%,#f1efe6 45%,#f3e6e0 75%,#eef0e4 100%);
  }
  .screen--home{left:38px}
  .screen--menu{left:596px}
  .screen__backdrop{position:absolute;inset:0;
    background:radial-gradient(ellipse at 30% 70%,rgba(170,190,130,.25),transparent 60%),
               radial-gradient(ellipse at 75% 85%,rgba(220,120,110,.18),transparent 55%);}
  .shape{position:absolute;left:0;top:0}
  .topbar{
    position:absolute;left:36px;top:26px;width:426px;height:60px;border-radius:12px;
    background:var(--sage-soft);display:flex;align-items:center;padding:0 18px;
  }
  .brand{display:flex;flex-direction:column;line-height:1}
  .brand__name{font-weight:700;font-size:30px;color:var(--ink);letter-spacing:.5px}
  .brand__tag{font-size:8px;color:var(--ink);margin-top:2px;padding-left:16px}
  .avatar{position:absolute;right:66px;top:8px;width:44px;height:44px;border-radius:50%;
    background:linear-gradient(160deg,#c9c4bb,#8b8176)}
  .menu-icon{position:absolute;right:14px;top:18px}
  .hero-photo{position:absolute;left:118px;top:180px;width:270px;height:270px;border-radius:50%;
    background:radial-gradient(circle at 45% 45%,#8fbf4a 0%,#5e9a2c 45%,#b84a36 70%,#f4f4f2 72%,#e9e9e6 100%);
    box-shadow:0 8px 20px rgba(0,0,0,.2)}
  .carousel-bars{position:absolute;left:64px;top:528px;display:flex;gap:14px}
  .carousel-bars span{width:62px;height:8px;border-radius:4px;background:var(--ink)}
  .carousel-bars span.is-active{background:var(--dot-olive)}
  .welcome__title{position:absolute;left:0;width:100%;top:596px;text-align:center;
    font-weight:700;font-size:38px;color:var(--olive-ink);letter-spacing:.5px}
  .welcome__text{position:absolute;left:20px;right:20px;top:664px;text-align:center;
    font-size:25px;line-height:34px;color:#2c2c2c}
  .btn{position:absolute;left:79px;width:338px;height:77px;border-radius:20px;display:flex;
    align-items:center;justify-content:center;color:var(--white);font-size:27px;font-weight:500}
  .btn--create{top:849px;background:var(--orange)}
  .btn--salads{top:955px;background:var(--slate)}
  .back{position:absolute;left:46px;top:120px}
  .page-title{position:absolute;left:46px;top:150px;font-size:40px;font-weight:600;color:var(--olive-ink)}
  .dish{position:absolute;width:230px}
  .dish__name{font-size:27px;font-weight:600;color:var(--olive-ink)}
  .dish__desc{font-size:16.5px;line-height:23px;color:var(--muted);text-align:justify;margin-top:8px}
  .dish__meta{display:flex;align-items:center;gap:6px;margin-top:10px;font-size:19px;font-weight:500;color:var(--ink)}
  .dish__cart{display:inline-block;margin-top:8px;font-size:19px;font-weight:500;color:var(--ink);text-decoration:underline}
  .dish-photo{position:absolute;border-radius:50%;
    background:radial-gradient(ellipse at 50% 40%,#6ea33a 0%,#c5452f 40%,#8dbb55 55%,#f5f5f3 62%,#dedede 100%);
    box-shadow:0 10px 14px rgba(0,0,0,.15)}
  .pager{position:absolute;left:200px;top:964px;display:flex;gap:16px}
  .pager span{width:18px;height:18px;border-radius:50%;background:#c4c4c4}
  .pager span.is-active{background:var(--olive-ink)}
</style>
</head>
<body>

<section class="screen screen--home">
  <div class="screen__backdrop" role="img" aria-label="Soft blurred background photo of fresh salad"></div>
  <svg class="shape" width="510" height="480" viewBox="0 0 510 480">
    <path d="M0 0H510V330Q300 470 0 430Z" fill="var(--sage)"/>
  </svg>
  <header class="topbar">
    <div class="brand"><span class="brand__name">Verdo</span><span class="brand__tag">Fresh Every Day</span></div>
    <div class="avatar" role="img" aria-label="User profile photo"></div>
    <svg class="menu-icon" width="42" height="26" viewBox="0 0 42 26"><g stroke="var(--ink)" stroke-width="3.5" stroke-linecap="round"><line x1="2" y1="2" x2="40" y2="2"/><line x1="12" y1="13" x2="40" y2="13"/><line x1="2" y1="24" x2="40" y2="24"/></g></svg>
  </header>
  <div class="hero-photo" role="img" aria-label="Plate of fresh green salad with tomatoes and beef, seen from above"></div>
  <div class="carousel-bars"><span></span><span class="is-active"></span><span></span><span></span></div>
  <h1 class="welcome__title">WELCOME TO VERDO</h1>
  <p class="welcome__text">Lorem ipsum dolor sit amet, consectetur adipiscing elit, sed do eiusmod tempor incididunt ut labore et dolore magna aliqua.</p>
  <a class="btn btn--create">Create Your Salad</a>
  <a class="btn btn--salads">Our Salads</a>
</section>

<section class="screen screen--menu">
  <div class="screen__backdrop" role="img" aria-label="Soft blurred background photo of fresh salad"></div>
  <svg class="shape" width="510" height="1124" viewBox="0 0 510 1124">
    <path d="M0 0H510V20Q400 230 0 252Z" fill="var(--sage-soft)"/>
    <ellipse cx="260" cy="1140" rx="250" ry="120" fill="var(--sage-soft)"/>
  </svg>
  <header class="topbar">
    <div class="brand"><span class="brand__name">Verdo</span><span class="brand__tag">Fresh Every Day</span></div>
    <div class="avatar" role="img" aria-label="User profile photo"></div>
    <svg class="menu-icon" width="42" height="26" viewBox="0 0 42 26"><g stroke="var(--ink)" stroke-width="3.5" stroke-linecap="round"><line x1="2" y1="2" x2="40" y2="2"/><line x1="12" y1="13" x2="40" y2="13"/><line x1="2" y1="24" x2="40" y2="24"/></g></svg>
  </header>
  <svg class="back" width="30" height="24" viewBox="0 0 30 24"><g stroke="var(--ink)" stroke-width="3" fill="none" stroke-linecap="round" stroke-linejoin="round"><path d="M28 12H3"/><path d="M12 3L3 12l9 9"/></g></svg>
  <h2 class="page-title">Our Salad</h2>

  <div class="dish-photo" style="left:40px;top:318px;width:190px;height:90px" role="img" aria-label="Bowl of chopped vegetable salad"></div>
  <article class="dish" style="left:268px;top:264px">
    <h3 class="dish__name">Lorem Ipsum</h3>
    <p class="dish__desc">Lorem ipsum dolor sit amet, consectetur adipisc elit, sed do eiusmod</p>
    <div class="dish__meta">
      <svg width="88" height="16" viewBox="0 0 88 16"><g fill="var(--star)"><path id="s" d="M8 0l2.4 5 5.6.6-4.2 3.8 1.2 5.6L8 12.2 3 15l1.2-5.6L0 5.6 5.6 5z"/><use href="#s" x="18"/><use href="#s" x="36"/><use href="#s" x="54"/></g><use href="#s" x="72" fill="var(--star-off)"/></svg>
      <span>[5.0] &nbsp;|&nbsp; 3</span>
      <svg width="16" height="18" viewBox="0 0 16 18"><circle cx="8" cy="5" r="4.5" fill="var(--ink)"/><path d="M0 18c0-5 3.5-7 8-7s8 2 8 7z" fill="var(--ink)"/></svg>
    </div>
    <a class="dish__cart">Add To Cart</a>
  </article>

  <article class="dish" style="left:21px;top:504px">
    <h3 class="dish__name">Lorem Ipsum</h3>
    <p class="dish__desc">Lorem ipsum dolor sit amet, consectetur adipisc elit, sed do eiusmod</p>
    <div class="dish__meta">
      <svg width="88" height="16" viewBox="0 0 88 16"><g fill="var(--star)"><use href="#s"/><use href="#s" x="18"/><use href="#s" x="36"/><use href="#s" x="54"/></g><use href="#s" x="72" fill="var(--star-off)"/></svg>
      <span>[5.0] &nbsp;|&nbsp; 3</span>
      <svg width="16" height="18" viewBox="0 0 16 18"><circle cx="8" cy="5" r="4.5" fill="var(--ink)"/><path d="M0 18c0-5 3.5-7 8-7s8 2 8 7z" fill="var(--ink)"/></svg>
    </div>
    <a class="dish__cart">Add To Cart</a>
  </article>
  <div class="dish-photo" style="left:258px;top:580px;width:198px;height:84px" role="img" aria-label="Plate of Greek salad with feta and olives"></div>

  <div class="dish-photo" style="left:48px;top:785px;width:180px;height:96px" role="img" aria-label="Bowl of mixed leaf salad with shredded carrot"></div>
  <article class="dish" style="left:268px;top:743px">
    <h3 class="dish__name">Lorem Ipsum</h3>
    <p class="dish__desc">Lorem ipsum dolor sit amet, consectetur adipisc elit, sed do eiusmod</p>
    <div class="dish__meta">
      <svg width="88" height="16" viewBox="0 0 88 16"><g fill="var(--star)"><use href="#s"/><use href="#s" x="18"/><use href="#s" x="36"/><use href="#s" x="54"/></g><use href="#s" x="72" fill="var(--star-off)"/></svg>
      <span>[5.0] &nbsp;|&nbsp; 3</span>
      <svg width="16" height="18" viewBox="0 0 16 18"><circle cx="8" cy="5" r="4.5" fill="var(--ink)"/><path d="M0 18c0-5 3.5-7 8-7s8 2 8 7z" fill="var(--ink)"/></svg>
    </div>
    <a class="dish__cart">Add To Cart</a>
  </article>

  <div class="pager"><span></span><span class="is-active"></span><span></span><span></span></div>
</section>

</body>
</html>
```